New layout for printer ink webiste

We require fresh ,easy to navigate layout for our online shop, everything can be changed even the logo open to ideas, We are cut price printer cartridge retailer pos is price, quality and speed of delivery. Design is for magento store website www.quillmora.ie (landing page and product page).

Target Market(s)

printer owners

Industry/Entity Type

Printer

Number of Pages Required

2 page

Requirements
Must have
• clear pricing, and what we sell.
Nice to have
• must keep quick search menu, maybe different layout
Should not have
• too much going on

```html
<!DOCTYPE html>
<html lang="en">
<head>
<meta charset="utf-8">
<title>Quillmora – Ink and Toner Supplies</title>
<link href="https://fonts.googleapis.com/css2?family=Open+Sans:wght@300;400;600;700;800&display=swap" rel="stylesheet">
<style>
:root{
  --blue:#29abe2;
  --red:#e8412a;
  --orange:#ffa500;
  --ink:#222222;
  --text:#555555;
  --bar:#3a3a3a;
  --footer:#414141;
  --footer-text:#dddddd;
  --line:#cccccc;
  --white:#ffffff;
}
*{box-sizing:border-box;margin:0;padding:0}
html,body{width:1200px;height:2459px;overflow:hidden}
body{position:relative;background:var(--white);font-family:"Open Sans",Arial,sans-serif;color:var(--text)}
.abs{position:absolute}

/* top bar */
.topbar{left:0;top:0;width:1200px;height:41px;background:var(--bar)}
.brand{left:90px;top:6px;color:var(--white);font-size:22px;font-weight:700;letter-spacing:.5px}
.cart{left:993px;top:0;width:108px;height:41px;border-left:1px solid #555;border-right:1px solid #555;color:var(--white);font-size:12px;font-weight:700;display:flex;align-items:center;justify-content:center;gap:8px}

/* hero */
.hero-title{left:101px;top:134px;font-size:43px;font-weight:700;color:var(--blue);letter-spacing:.5px}
.hero-sub{left:101px;top:183px;font-size:36px;font-weight:300;color:var(--ink)}
.features{left:101px;top:256px;display:flex;gap:36px}
.feature{display:flex;align-items:center;gap:12px;font-size:21px;line-height:26px;color:#444}
.search{left:105px;top:341px;width:380px;height:47px;border:1px solid #777;display:flex;align-items:center;justify-content:space-between;padding:0 18px;font-size:14px;font-style:italic;color:#444}
.hero-photo{left:623px;top:41px;width:577px;height:470px;background:radial-gradient(ellipse at 55% 60%,#9ea4ad 0%,#d9dbde 55%,#ffffff 80%)}

/* about band */
.about{left:0;top:521px;width:1200px;height:484px;background:linear-gradient(90deg,#b9bdc2 0%,#8a8f96 45%,#6f7b8c 65%,#a59d90 100%)}
.about-inner{left:250px;top:690px;width:700px;text-align:center;color:var(--white)}
.about-inner h2{font-size:31px;font-weight:700;line-height:36px}
.about-inner h3{font-size:31px;font-weight:300;line-height:38px}
.about-inner p{margin:8px auto 0;width:660px;font-size:19px;line-height:35px}
.btn-outline{left:482px;top:897px;width:226px;height:54px;border:2px solid var(--white);color:var(--white);font-size:22px;display:flex;align-items:center;justify-content:center}

/* products */
.section-title{left:0;top:1066px;width:1200px;text-align:center;font-size:31px;color:var(--ink);font-weight:300}
.section-title b{font-weight:700}
.section-lead{left:310px;top:1118px;width:580px;text-align:center;font-size:16px;line-height:27px}
.arrow{width:42px;height:42px;border-radius:50%;background:#e6e6e6;display:flex;align-items:center;justify-content:center}
.product{width:260px;text-align:center}
.product-img{margin:0 auto;height:152px}
.product h4{margin-top:26px;font-size:16px;font-weight:700;color:var(--ink)}
.product p{margin:8px auto 0;width:252px;font-size:13px;line-height:22px;text-align:center}
.buy{margin:14px auto 0;width:111px;height:27px;background:var(--orange);color:var(--white);font-size:8px;font-weight:700;display:flex;align-items:center;justify-content:center}

/* promo */
.video{left:102px;top:1601px;width:587px;height:418px;background:linear-gradient(160deg,#e4e4e4 0%,#f4f4f4 50%,#d8d8d8 100%)}
.play{left:331px;top:1754px;width:114px;height:114px;border-radius:50%;border:5px solid var(--white);display:flex;align-items:center;justify-content:center}
.perk{left:721px;width:384px;display:flex;align-items:center;color:var(--white);font-size:21px;font-weight:700;line-height:27px}
.perk .icon{width:150px;display:flex;justify-content:center}
.perk-blue{top:1605px;height:88px;background:var(--blue)}
.perk-red{top:1696px;height:97px;background:var(--red)}
.perk-black{top:1796px;height:74px;background:#000}
.combo{left:721px;top:1883px;width:384px;height:133px;border:2px solid var(--line);display:flex;align-items:center}
.combo-img{margin-left:24px;width:100px;height:92px;background:linear-gradient(120deg,#4fb9e6,#e0448f 50%,#f2de3c)}
.combo-text{margin-left:26px;text-align:center;font-size:21px;font-weight:700;color:var(--ink);line-height:26px}
.combo-text span{display:block;font-size:36px;font-weight:800;color:var(--blue);line-height:42px}

/* assurance strip */
.assure{display:flex;align-items:center;gap:6px;font-weight:800;color:var(--ink);line-height:17px}

/* footer */
.footer{left:0;top:2154px;width:1200px;height:305px;background:var(--footer)}
.fcol{top:2190px;color:var(--footer-text)}
.fcol h5{font-size:13.5px;font-weight:600;margin-bottom:12px;color:var(--white)}
.fcol li{list-style:none;font-size:10px;line-height:18px}
.fcol p{font-size:9.5px;line-height:15px;width:200px;margin-bottom:6px}
.social{display:flex;gap:6px;margin-top:6px}
.social i{width:17px;height:17px;border:1px solid var(--footer-text);border-radius:50%}
.fdivider{left:84px;top:2378px;width:1029px;height:1px;background:#666}
.copyright{left:84px;top:2396px;font-size:10px;color:var(--footer-text)}
.pay{left:833px;top:2390px;display:flex;gap:8px}
.pay span{height:24px;padding:0 6px;background:var(--white);color:#1d3f8f;font-size:10px;font-weight:700;display:flex;align-items:center}
</style>
</head>
<body>

<header class="abs topbar"></header>
<div class="abs brand">quillmora.ie</div>
<div class="abs cart">
  <svg width="12" height="14" viewBox="0 0 12 14"><rect x="1" y="6" width="10" height="8" fill="#fff"/><path d="M3 6V4a3 3 0 0 1 6 0v2" stroke="#fff" stroke-width="1.6" fill="none"/></svg>
  MY CART
</div>

<section>
  <div class="abs hero-photo" role="img" aria-label="Printer with a row of colour ink cartridges and printed photos"></div>
  <h1 class="abs hero-title">BEST SOURCE</h1>
  <div class="abs hero-sub">FOR INK AND TONER SUPPLIES</div>
  <div class="abs features">
    <div class="feature">
      <svg width="38" height="50" viewBox="0 0 38 50"><rect x="4" y="8" width="26" height="38" fill="none" stroke="#29abe2" stroke-width="3"/><rect x="10" y="2" width="14" height="8" fill="#29abe2"/><path d="M17 22c-4 6-5 8-5 10a5 5 0 0 0 10 0c0-2-1-4-5-10z" fill="#29abe2"/></svg>
      <span>Best<br>Seller</span>
    </div>
    <div class="feature">
      <svg width="44" height="50" viewBox="0 0 44 50"><rect x="10" y="4" width="22" height="32" transform="rotate(30 21 20)" fill="none" stroke="#29abe2" stroke-width="3"/><path d="M10 34c-4 6-5 8-5 10a5 5 0 0 0 10 0c0-2-1-4-5-10z" fill="#29abe2"/></svg>
      <span>Authentic<br>Product</span>
    </div>
    <div class="feature">
      <svg width="44" height="50" viewBox="0 0 44 50"><circle cx="24" cy="18" r="13" fill="none" stroke="#29abe2" stroke-width="3"/><text x="24" y="24" text-anchor="middle" font-size="16" font-weight="700" fill="#29abe2" font-family="Open Sans,sans-serif">$</text><path d="M2 38h12l10 4h14v4H20L2 44z" fill="#29abe2"/></svg>
      <span>Reasonable<br>Price</span>
    </div>
  </div>
  <div class="abs search">
    <span>Search item...</span>
    <svg width="22" height="22" viewBox="0 0 22 22"><circle cx="9" cy="9" r="7" fill="none" stroke="#222" stroke-width="3"/><path d="M14 14l7 7" stroke="#222" stroke-width="3.5"/></svg>
  </div>
</section>

<section>
  <div class="abs about" role="img" aria-label="Two colleagues smiling while reading a printed sheet in a bright office"></div>
  <div class="abs about-inner">
    <h2>ABOUT US</h2>
    <h3>OUR SPECIALITY</h3>
    <p>It is a long established fact that a reader will be distracted by the readable content of a page when looking at its layout. The point of using Lorem Ipsum is that it has a more-or-less normal distribution of letters,</p>
  </div>
  <div class="abs btn-outline">Learn More+</div>
</section>

<section>
  <h2 class="abs section-title"><b>LOOK AT</b> OUR PRODUCTS</h2>
  <p class="abs section-lead">It is a long established fact that a reader will be distracted by the readable content of a page when looking at its layout.</p>

  <div class="abs arrow" style="left:107px;top:1275px"><svg width="12" height="16" viewBox="0 0 12 16"><path d="M9 2L3 8l6 6" stroke="#fff" stroke-width="2" fill="none"/></svg></div>
  <div class="abs arrow" style="left:1002px;top:1275px"><svg width="12" height="16" viewBox="0 0 12 16"><path d="M3 2l6 6-6 6" stroke="#fff" stroke-width="2" fill="none"/></svg></div>

  <div class="abs product" style="left:137px;top:1213px">
    <div class="product-img" role="img" aria-label="Black ink cartridge in retail pack" style="width:96px;background:linear-gradient(#1c1c1c,#3a3a3a)"></div>
    <h4>QM 564 INK CARTRIDGES</h4>
    <p>It is a long established fact that a reader will be distracted by the readable content of a page when looking.</p>
    <div class="buy">BUY NOW</div>
  </div>
  <div class="abs product" style="left:434px;top:1213px">
    <div class="product-img" role="img" aria-label="Set of four colour ink cartridges" style="width:208px;background:linear-gradient(90deg,#3fb2e0,#e1346b 35%,#f0d43a 65%,#1b2a6b)"></div>
    <h4>QM 564 INK CARTRIDGES</h4>
    <p>It is a long established fact that a reader will be distracted by the readable content of a page when looking.</p>
    <div class="buy">BUY NOW</div>
  </div>
  <div class="abs product" style="left:739px;top:1213px">
    <div class="product-img" role="img" aria-label="Set of refillable ink cartridges" style="width:170px;background:linear-gradient(90deg,#9fd4ea,#e6a1c0 35%,#efe38c 65%,#555)"></div>
    <h4>QM 564 INK CARTRIDGES</h4>
    <p>It is a long established fact that a reader will be distracted by the readable content of a page when looking.</p>
    <div class="buy">BUY NOW</div>
  </div>
</section>

<section>
  <div class="abs video" role="img" aria-label="Video still of a white printer with colour cartridges against a brick wall"></div>
  <div class="abs play"><svg width="44" height="50" viewBox="0 0 44 50"><path d="M6 3l34 22L6 47z" fill="#fff"/></svg></div>

  <div class="abs perk perk-blue">
    <div class="icon"><svg width="44" height="50" viewBox="0 0 44 50"><rect x="12" y="4" width="22" height="30" transform="rotate(30 23 19)" fill="none" stroke="#fff" stroke-width="3"/><path d="M10 34c-4 6-5 8-5 10a5 5 0 0 0 10 0c0-2-1-4-5-10z" fill="#fff"/></svg></div>
    <span>GRADE A<br>INKS USED</span>
  </div>
  <div class="abs perk perk-red">
    <div class="icon"><svg width="70" height="70" viewBox="0 0 70 70"><circle cx="35" cy="35" r="30" fill="#fff"/><circle cx="35" cy="35" r="22" fill="none" stroke="#e8412a" stroke-width="3"/></svg></div>
    <span>1 YEAR<br>WARRANTY</span>
  </div>
  <div class="abs perk perk-black">
    <div class="icon"><svg width="50" height="50" viewBox="0 0 50 50"><circle cx="25" cy="25" r="20" fill="#fff"/></svg></div>
    <span>19,000<br>CUSTOMER</span>
  </div>
  <div class="abs combo">
    <div class="combo-img" role="img" aria-label="Three colour ink cartridges"></div>
    <div class="combo-text">BUILD YOUR OWN<span>COMBO</span></div>
  </div>
</section>

<section>
  <div class="abs assure" style="left:104px;top:2070px">
    <span style="background:var(--red);color:#fff;font-size:24px;padding:2px 6px">Price</span>
    <span style="font-size:18px">BEST<br><small style="font-size:13px">ONLINE</small></span>
  </div>
  <div class="abs assure" style="left:282px;top:2072px">
    <span style="font-size:16px">FREE <span style="color:var(--red)">SHIPPING</span><br>&nbsp;&nbsp;&nbsp;&nbsp;OVER €30</span>
    <svg width="40" height="30" viewBox="0 0 40 30"><rect x="2" y="6" width="22" height="16" fill="none" stroke="#222" stroke-width="2.5"/><path d="M24 11h8l6 6v5H24z" fill="none" stroke="#222" stroke-width="2.5"/><circle cx="10" cy="25" r="3.5" fill="#fff" stroke="#222" stroke-width="2"/><circle cx="31" cy="25" r="3.5" fill="#fff" stroke="#222" stroke-width="2"/></svg>
  </div>
  <div class="abs assure" style="left:488px;top:2066px">
    <span style="font-size:15px;text-align:center">CARTRIDGES FROM<br>ISO-9001 SUPPLIER</span>
    <svg width="44" height="44" viewBox="0 0 44 44"><circle cx="22" cy="22" r="18" fill="#cfd6dc"/></svg>
  </div>
  <div class="abs assure" style="left:758px;top:2072px">
    <span style="font-size:18px;text-align:center">1 YEAR<br><small style="color:var(--red);font-size:12px">GUARANTEE</small></span>
    <svg width="48" height="48" viewBox="0 0 48 48"><circle cx="24" cy="22" r="18" fill="#c8302a"/></svg>
  </div>
  <div class="abs assure" style="left:974px;top:2068px">
    <span style="font-size:24px;color:var(--red);text-align:center">100%<br><small style="color:#222;font-size:11px;letter-spacing:3px">SECURE</small></span>
    <svg width="30" height="34" viewBox="0 0 30 34"><path d="M8 14V9a7 7 0 0 1 14 0v5" stroke="#999" stroke-width="3" fill="none"/><rect x="4" y="14" width="22" height="18" fill="#e9a326"/></svg>
  </div>
</section>

<footer>
  <div class="abs footer"></div>
  <div class="abs fcol" style="left:102px">
    <h5>ABOUT US</h5>
    <p>It is a long established fact that a reader will be distracted by the readable content of a page when looking.</p>
    <p>It is a long established fact that a reader will be distracted please use it design purpose.</p>
  </div>
  <div class="abs fcol" style="left:356px">
    <h5>PRODUCT CATEGORIES</h5>
    <ul><li>› Northjet Cartridge</li><li>› Kelbrook Cartridge</li><li>› Varlo Cartridge</li><li>› Estrel Cartridge</li><li>› Dunmore Cartridge</li><li>› Lexfield Cartridge</li></ul>
  </div>
  <div class="abs fcol" style="left:565px">
    <h5>SUPPORT</h5>
    <ul><li>› Download drivers</li><li>› Support &amp; troubleshooting</li><li>› Forum</li><li>› Register your product</li><li>› Certification</li><li>› Authorize service center</li></ul>
  </div>
  <div class="abs fcol" style="left:741px">
    <h5>COMPANY RULES</h5>
    <ul><li>› Terms &amp; conditions</li><li>› Rules &amp; regulations</li><li>› Privacy policy</li><li>› Help</li></ul>
  </div>
  <div class="abs fcol" style="left:931px">
    <h5>CONTACT US</h5>
    <ul><li>☎ 01-555-0142</li><li>☏ 01-555-0187</li><li>✉ hello@quillmora.ie</li></ul>
    <div class="social"><i></i><i></i><i></i><i></i></div>
  </div>
  <div class="abs fdivider"></div>
  <div class="abs copyright">Copyright © 2014 quillmora.ie. All rights reserved.</div>
  <div class="abs pay"><span>PayWell</span><span>Vantra</span><span>Merida</span><span>Lasko</span><span>Mestra</span></div>
</footer>

</body>
</html>
```